Torvale Works- Plumbing Business Card

We need a business card design for a new company that services Canberra and surrounds. We are a professional family-owned plumbing company who has 20+ years' experience. We would like to use our logo as well as the colours black, white, grey and the signature green. The final design needs to communicate professional, high-end, plumbing with reliable service. We provide obligation free quotes and are open 24/7. Services include: Bathroom/kitchen renovations, drainage, stormwater, water leaks, plumbing maintenance, water tanks and septics.

Target Market(s)

Homeowners, real estate agents, builders, small business owners

Industry/Entity Type

Plumbing & Construction

Font styles to use
Serif
Sans Serif

Colors
59FF00
82FF00
B8FF75
E3FFCB
F4FFEA

Requirements
Must have
• Must have logo, example of services and contact details

```html
<!DOCTYPE html>
<html lang="en">
<head>
<meta charset="utf-8">
<title>Torvale Works – Business Card</title>
<link rel="stylesheet" href="https://fonts.googleapis.com/css2?family=Jura:wght@500;600&display=swap">
<style>
  :root {
    --ink: #111111;
    --white: #ffffff;
    --green-deep: #1e9a12;
    --green-brand: #59ff00;
    --green-bright: #82ff00;
    --green-soft: #b8ff75;
    --green-pale: #e3ffcb;
    --green-mist: #f4ffea;
    --green-mark: #149a0c;
  }
  html, body {
    margin: 0;
    padding: 0;
    overflow: hidden;
    background: var(--white);
  }
  .card {
    position: relative;
    width: 1200px;
    height: 800px;
    overflow: hidden;
    background: var(--white);
    font-family: "Jura", sans-serif;
    color: var(--ink);
  }
  .card__panel {
    position: absolute;
    inset: 0;
    width: 1200px;
    height: 800px;
  }
  .brand {
    position: absolute;
    left: 132px;
    top: 172px;
  }
  .brand__name {
    margin: 0;
    font-weight: 500;
    font-size: 68px;
    line-height: 1;
    letter-spacing: 2px;
  }
  .brand__name-accent { color: var(--green-deep); }
  .brand__tagline {
    margin: 8px 0 0;
    font-weight: 500;
    font-size: 34px;
    line-height: 45px;
    letter-spacing: 2px;
    color: var(--green-deep);
  }
  .contacts {
    position: absolute;
    left: 134px;
    top: 383px;
    margin: 0;
    font-weight: 500;
    font-size: 30px;
    letter-spacing: 1.8px;
  }
  .contacts__row {
    display: flex;
    height: 52px;
    align-items: center;
  }
  .contacts__name { width: 163px; }
  .contacts__phone { margin: 0; }
  .links {
    position: absolute;
    left: 132px;
    top: 514px;
    font-weight: 500;
    font-size: 30px;
    letter-spacing: 1.8px;
  }
  .links__item {
    display: block;
    height: 52px;
    line-height: 52px;
    color: var(--ink);
    text-decoration: none;
  }
  .mark {
    position: absolute;
    left: 800px;
    top: 330px;
    display: flex;
    align-items: center;
    gap: 22px;
  }
  .mark__dot {
    width: 150px;
    height: 150px;
    border-radius: 50%;
    background: var(--green-mark);
  }
  .mark__name {
    margin: 0;
    font-weight: 600;
    font-size: 48px;
    letter-spacing: 2px;
    color: var(--ink);
  }
</style>
</head>
<body>
  <main class="card">
    <svg class="card__panel" viewBox="0 0 1200 800" aria-hidden="true">
      <defs>
        <linearGradient id="panelFill" x1="0" y1="0" x2="0.3" y2="1">
          <stop offset="0" stop-color="#e3ffcb"/>
          <stop offset="0.45" stop-color="#b8ff75"/>
          <stop offset="1" stop-color="#82ff00"/>
        </linearGradient>
      </defs>
      <path d="M950 0 H1200 V800 H922 L688 420 Q660 362 700 312 Z" fill="#b8ff75" opacity="0.75"/>
      <path d="M990 0 H1200 V800 H946 L712 420 Q686 366 724 320 Z" fill="url(#panelFill)"/>
      <path d="M955 0 H990 L724 320 Q712 334 704 348 Z" fill="#59ff00"/>
    </svg>

    <header class="brand">
      <h1 class="brand__name">TORVALE <span class="brand__name-accent">WORKS</span></h1>
      <p class="brand__tagline">Plumbing Services and<br>Bathroom Renovations</p>
    </header>

    <dl class="contacts">
      <div class="contacts__row"><dt class="contacts__name">Marcus</dt><dd class="contacts__phone">0412 555 018</dd></div>
      <div class="contacts__row"><dt class="contacts__name">Declan</dt><dd class="contacts__phone">0455 210 374</dd></div>
    </dl>

    <nav class="links">
      <a class="links__item" href="#">torvaleworks.com.au</a>
      <a class="links__item" href="#">info@torvaleworks.com</a>
    </nav>

    <div class="mark">
      <span class="mark__dot" aria-hidden="true"></span>
      <p class="mark__name">TVW</p>
    </div>
  </main>
</body>
</html>
```